New Advertising Company Business Card

A two sided business card. One side with logo only and the other side with my information and maybe my logo again. Looking for something unique and creative, but not too busy. Info would include my name(Marcus Feldon), President, phone number, address, email address, and website. LOGO IS THE BLUE AND WHITE ONE.

Target Market(s)

CEO/VP Level Audience

Industry/Entity Type

Business

Contact Information for Business Card

In Description.

```html
<!DOCTYPE html>
<html lang="en">
<head>
<meta charset="utf-8">
<title>Harbor Advertising — Business Card</title>
<link href="https://fonts.googleapis.com/css2?family=Source+Sans+3:wght@400;600;700&display=swap" rel="stylesheet">
<style>
  :root {
    --brand-blue: #2a6db5;
    --ink: #1f1f22;
    --paper: #ffffff;
    --backdrop: #e9ebee;
    --rule: #2f72c0;
  }
  * { margin: 0; padding: 0; box-sizing: border-box; }
  html, body { width: 1200px; height: 1200px; overflow: hidden; }
  body {
    background: var(--backdrop);
    font-family: "Source Sans 3", "Myriad Pro", Arial, sans-serif;
    display: flex;
    flex-direction: column;
    align-items: center;
    justify-content: center;
    gap: 80px;
  }
  .card {
    width: 840px;
    height: 480px;
    position: relative;
    box-shadow: 0 6px 18px rgba(0,0,0,0.12);
  }
  /* Front side */
  .card--front {
    background: var(--brand-blue);
    display: flex;
    align-items: center;
    justify-content: center;
    gap: 26px;
  }
  .front-mark {
    width: 46px; height: 46px;
    border-radius: 50%;
    background: var(--paper);
  }
  .front-name {
    color: var(--paper);
    font-weight: 600;
    font-size: 64px;
    letter-spacing: 0.06em;
    text-transform: uppercase;
    line-height: 1;
  }
  /* Back side */
  .card--back {
    background: var(--paper);
    display: flex;
    align-items: center;
    padding: 0 60px 0 70px;
  }
  .back-brand {
    color: var(--ink);
    font-weight: 600;
    font-size: 27px;
    letter-spacing: 0.08em;
    text-transform: uppercase;
    line-height: 1.1;
    width: 190px;
  }
  .person {
    margin-left: 40px;
    margin-right: 34px;
    align-self: flex-end;
    margin-bottom: 150px;
  }
  .person__name {
    color: var(--ink);
    font-weight: 700;
    font-size: 40px;
    line-height: 1.05;
    white-space: nowrap;
  }
  .person__title {
    color: var(--brand-blue);
    font-weight: 700;
    font-size: 26px;
  }
  .contact {
    border-left: 2px solid var(--rule);
    padding-left: 22px;
    list-style: none;
    color: var(--brand-blue);
    font-size: 19px;
    line-height: 1.55;
  }
  .contact li { display: flex; align-items: flex-start; gap: 10px; }
  .contact svg { width: 16px; height: 16px; flex: none; margin-top: 6px; fill: var(--ink); }
  .contact .no-icon { padding-left: 26px; }
</style>
</head>
<body>
  <section class="card card--front" aria-label="Card front">
    <span class="front-mark" aria-hidden="true"></span>
    <span class="front-name">Harbor Advertising</span>
  </section>

  <section class="card card--back" aria-label="Card back">
    <div class="back-brand">Harbor<br>Advertising</div>
    <div class="person">
      <div class="person__name">Marcus Feldon</div>
      <div class="person__title">President</div>
    </div>
    <ul class="contact">
      <li class="no-icon">4170 Cedar Ridge Ave, Ste 210</li>
      <li>
        <svg viewBox="0 0 16 16" aria-hidden="true"><path d="M8 0a5.5 5.5 0 0 0-5.5 5.5C2.5 10 8 16 8 16s5.5-6 5.5-10.5A5.5 5.5 0 0 0 8 0zm0 8a2.5 2.5 0 1 1 0-5 2.5 2.5 0 0 1 0 5z"/></svg>
        Fairview, CA 92044
      </li>
      <li>
        <svg viewBox="0 0 16 16" aria-hidden="true"><path d="M3.6 1 6 4.2 4.6 5.9a9 9 0 0 0 5.5 5.5L11.8 10 15 12.4 13.4 15C6.6 14.6 1.4 9.4 1 2.6z"/></svg>
        555.201.4387
      </li>
      <li>
        <svg viewBox="0 0 16 16" aria-hidden="true"><path d="M1 3h14v10H1zm1.5 1.2v.3L8 8.6l5.5-4.1v-.3z"/></svg>
        hello@harboradco.com
      </li>
      <li>
        <svg viewBox="0 0 16 16" aria-hidden="true"><circle cx="8" cy="8" r="7"/><path d="M1 8h14M8 1c-3 3.5-3 10.5 0 14M8 1c3 3.5 3 10.5 0 14" stroke="#fff" stroke-width="1.2" fill="none"/></svg>
        www.harboradco.com
      </li>
    </ul>
  </section>
</body>
</html>
```